deceased estate cleaning services and cosmetic renovating

house frontage signage design
cur flute sign will be 600mm x 450 mm and no larger
is to be mounted of fence out front of projects as advertizing

Target Market(s)

elderly people and there sibling that need help

Colors
cadf82
85cae6
fbed22
85acd3
ffcf3e

Requirements
Must have
• clear phone number, email and business Name and logo
Should not have
• to much info and NO dark colors

```html
<!DOCTYPE html>
<html lang="en">
<head>
<meta charset="utf-8">
<title>Tidyhome – Fence Sign</title>
<link rel="stylesheet" href="https://fonts.googleapis.com/css2?family=Arimo:wght@400;700&family=EB+Garamond:ital,wght@0,500;1,400&display=swap">
<style>
  :root {
    --ink: #0b0b0b;
    --forest: #1d4a2b;
    --rule-green: #a3c23a;
    --band-left: #6ea243;
    --band-right: #a2c43c;
    --mark-green: #6fb04a;
    --paper: #ffffff;
  }
  * { margin: 0; padding: 0; box-sizing: border-box; }
  html, body { width: 1200px; height: 900px; overflow: hidden; background: var(--paper); }
  .sign {
    position: relative;
    width: 1200px;
    height: 900px;
    background: var(--paper);
    font-family: "Arimo", Arial, sans-serif;
    color: var(--ink);
  }
  .tagline {
    position: absolute;
    top: 22px; left: 0; width: 100%;
    text-align: center;
    font-family: "EB Garamond", Georgia, serif;
    font-style: italic;
    font-size: 56px;
    color: var(--forest);
    letter-spacing: -0.5px;
    white-space: nowrap;
  }
  .brand-dot {
    position: absolute;
    top: 135px; left: 535px;
    width: 130px; height: 130px;
    border-radius: 50%;
    background: var(--mark-green);
  }
  .brand-name {
    position: absolute;
    top: 302px; left: 0; width: 100%;
    text-align: center;
    font-family: "EB Garamond", Georgia, serif;
    font-weight: 500;
    font-size: 60px;
    letter-spacing: 1px;
    color: var(--ink);
    white-space: nowrap;
  }
  .rule {
    position: absolute;
    left: 86px; width: 1029px; height: 4px;
    background: var(--rule-green);
  }
  .rule--top { top: 405px; }
  .rule--bottom { top: 563px; }
  .services {
    position: absolute;
    top: 415px; left: 0; width: 100%;
    text-align: center;
    font-weight: 700;
    font-size: 54px;
    line-height: 74px;
    white-space: nowrap;
  }
  .values {
    position: absolute;
    top: 598px; left: 0; width: 100%;
    text-align: center;
    font-family: "EB Garamond", Georgia, serif;
    font-style: italic;
    font-size: 53px;
    color: var(--forest);
    word-spacing: 4px;
    white-space: nowrap;
  }
  .phone {
    position: absolute;
    top: 693px; left: 0; width: 1190px;
    text-align: center;
    font-weight: 700;
    font-size: 88px;
    letter-spacing: -1px;
    line-height: 1;
    white-space: nowrap;
  }
  .recycle-icon {
    position: absolute;
    top: 667px; left: 1045px;
    width: 84px; height: 84px;
  }
  .recycle-label {
    position: absolute;
    top: 762px; left: 995px; width: 185px;
    text-align: center;
    font-size: 22px;
    white-space: nowrap;
  }
  .contact-band {
    position: absolute;
    left: 0; top: 806px;
    width: 1200px; height: 94px;
    display: flex;
  }
  .contact-band__cell {
    display: flex; align-items: center; justify-content: center;
    font-weight: 700;
    font-size: 43px;
    color: var(--ink);
    white-space: nowrap;
  }
  .contact-band__cell--email { width: 599px; background: var(--band-left); }
  .contact-band__cell--web { width: 601px; background: var(--band-right); }
</style>
</head>
<body>
  <main class="sign">
    <p class="tagline">We’re here to help declutter your life</p>

    <div class="brand-dot" aria-hidden="true"></div>
    <h1 class="brand-name">TIDYHOME</h1>

    <div class="rule rule--top"></div>
    <h2 class="services">Deceased Estate Cleanups<br>House Maintenance &amp; Cosmetic Repairs</h2>
    <div class="rule rule--bottom"></div>

    <p class="values">• Quality • Pride • Professionalism</p>

    <p class="phone">0400 123 456</p>

    <svg class="recycle-icon" role="img" aria-label="Recycling symbol" viewBox="0 0 84 84">
      <circle cx="42" cy="42" r="40" fill="#1a6b3a"/>
    </svg>
    <p class="recycle-label">Always Recycle</p>

    <footer class="contact-band">
      <div class="contact-band__cell contact-band__cell--email">info@tidyhome.com.au</div>
      <div class="contact-band__cell contact-band__cell--web">www.tidyhome.com.au</div>
    </footer>
  </main>
</body>
</html>
```